Service Menu refresh 2018 Update of menu pricing

We currently have service menus as attached. We will be updating our look via our homepage image, our service menu and our in-house beverage and treatment menu.
We are a natural and sustainable hair salon group and moving more towards head spa which consists of treatments, beauty, tanning as well as your traditional hair services. Our imagery needs to reflect our efforts in spa treatments in the hair and scalp area and use natural materials and colours reflecting sustainability.
Velin is the brand we stock and promote.

Target Market(s)

Men or women interesting in personal maintenance with natural and organic products and using sustainable practises

Industry/Entity Type

Hair And Beauty

Font styles to use
Sans Serif
Other font styles liked:
• Arial or Helvetica

Colors
9acb3c
abd037
cadf82
ffffff

Requirements
Must have
• Name on the front cover, locations on back cover
Nice to have
• Prestige feel, reflect male and female clients
Should not have
• Bold artificial writing or any type of cartoon images.
• Same images as existing menu.

```html
<!DOCTYPE html>
<html lang="en">
<head>
<meta charset="utf-8">
<title>greenhaven hair studios – Service Menu</title>
<link href="https://fonts.googleapis.com/css2?family=Arimo:ital,wght@0,400;0,700;1,400&family=Tinos:ital,wght@1,700&family=Great+Vibes&display=swap" rel="stylesheet">
<style>
:root{
  --green:#7cc142;
  --green-dark:#3f9a2f;
  --green-text:#3d9b35;
  --lime:#abd037;
  --pale:#cadf82;
  --white:#ffffff;
  --ink:#1d1d1d;
  --stage:#ececec;
}
*{margin:0;padding:0;box-sizing:border-box}
html,body{width:888px;height:1200px;overflow:hidden;background:var(--stage)}
body{position:relative;font-family:"Arimo",Arial,sans-serif;color:var(--ink)}
.spread{position:absolute;left:78px;width:730px;height:517px;overflow:hidden;background:var(--white)}
.spread--cover{top:54px}
.spread--menu{top:630px}
.abs{position:absolute}
.wave{position:absolute;left:0;top:0;width:730px;height:517px}

/* cover: back page */
.back-page{left:0;top:0;width:365px;height:517px;background:linear-gradient(160deg,#d6ebb0 0%,#e9f4d2 40%,#d2e8a8 100%)}
.foliage{left:170px;top:0;width:195px;height:150px;background:radial-gradient(ellipse at 70% 20%,rgba(124,193,66,.75),rgba(171,208,55,.25) 60%,transparent 75%)}
.quote{left:26px;top:42px;width:310px;font-family:"Tinos",serif;font-style:italic;font-weight:700;font-size:13.5px;line-height:18px;color:#1f2a14}
.locations-title{left:22px;top:117px;font-size:14px;font-weight:700;color:var(--green-text)}
.location{position:absolute;left:22px;font-size:9.6px;line-height:12.2px}
.location h3{font-size:10px;font-weight:700;color:var(--green-text);margin-bottom:1px}
.site-url{font-size:9.6px;font-weight:700;color:var(--white)}

/* cover: front page */
.front-page{left:365px;top:0;width:365px;height:517px;background:linear-gradient(180deg,#ffffff 0%,#f3f9ea 55%,#cfe6a7 100%)}
.brand{display:flex;align-items:center;gap:6px;font-size:22px;font-weight:400;color:#2a2a2a;white-space:nowrap}
.brand .dot{width:20px;height:20px;border-radius:50%;background:var(--green)}

/* menu */
.menu-bg{left:0;top:0;width:730px;height:517px;background:linear-gradient(180deg,#ffffff 0%,#f6f7f5 45%,#e3e8ea 70%,#dfe5e6 100%)}
.photo-beach{left:160px;top:250px;width:420px;height:200px;background:radial-gradient(ellipse at 50% 55%,rgba(120,110,105,.35),rgba(200,208,212,.2) 55%,transparent 75%)}
.photo-ingredients{left:500px;top:0;width:230px;height:110px;background:radial-gradient(ellipse at 45% 45%,rgba(160,130,80,.35),rgba(210,200,180,.2) 55%,transparent 75%)}
.menu-title{left:272px;top:64px;font-family:"Great Vibes",cursive;font-size:31px;color:var(--green-text)}
.section-head{position:absolute;font-size:10.5px;font-weight:700;color:var(--green-text)}
.section-head.main{font-size:12.5px}
.row{position:absolute;font-size:9px;line-height:11px;white-space:nowrap}
.row .p{position:absolute;top:0}
.left-col .row{left:28px}
.left-col .section-head{left:28px}
.left-col .p.s{left:151px}.left-col .p.m{left:186px}.left-col .p.l{left:219px}.left-col .p.xl{left:255px}
.right-col .row{left:398px}
.right-col .section-head{left:398px}
.right-col .p.s{left:177px}.right-col .p.m{left:212px}.right-col .p.l{left:245px}.right-col .p.xl{left:280px}
.row.big{font-size:10px}
.size-head{position:absolute;top:114px;font-size:10px;font-weight:700;color:var(--green-text)}
.note{position:absolute;left:398px;font-size:9px;line-height:11px}
.fine-print{left:140px;top:457px;width:450px;text-align:center;font-size:10px;line-height:12.5px;font-weight:700;color:var(--white)}
</style>
</head>
<body>

<section class="spread spread--cover">
  <div class="abs back-page"></div>
  <div class="abs foliage" role="img" aria-label="Sunlit green leaves on branches"></div>
  <p class="abs quote">“Choosing a gentler, greener way of living is a commitment, not just a label on a bottle”</p>
  <h2 class="abs locations-title">Our Locations</h2>

  <div class="location" style="top:150px"><h3>MAPLEBROOK</h3>Shop 42 Maplebrook Plaza, Birch Rd, Maplebrook<br>+61 (07) 3100 2401<br>maplebrook@greenhavenstudios.com</div>
  <div class="location" style="top:211px"><h3>FERNHILL</h3>Shop 87 Fernhill Centre, Wattle Road, Fernhill<br>+61 (07) 3100 2402<br>fernhill@greenhavenstudios.com</div>
  <div class="location" style="top:271px"><h3>RIVERBEND</h3>Shop 515 Riverbend Shopping Centre, Quarry Rd Riverbend.<br>+61 (07) 3100 2403<br>riverbend@greenhavenstudios.com</div>
  <div class="location" style="top:332px"><h3>LAKEVIEW</h3>Shop 706 Lakeview Square. Harbour St, Lakeview<br>+61 (07) 3100 2404<br>lakeview@greenhavenstudios.com</div>
  <div class="location" style="top:392px"><h3>LINDEN COMMUNITY HEALTH CENTRE</h3>Linden St, Ashby QLD 4000<br>+61 (07) 3100 2405<br>linden@greenhavenstudios.com</div>

  <div class="abs front-page"></div>
  <div class="abs brand" style="left:460px;top:22px"><span class="dot"></span>greenhaven hair studios</div>

  <svg class="wave" viewBox="0 0 730 517">
    <defs>
      <linearGradient id="portraitTone" x1="0" y1="0" x2="1" y2="1">
        <stop offset="0" stop-color="#9aa58c"/>
        <stop offset=".5" stop-color="#6b4a36"/>
        <stop offset="1" stop-color="#3f5a33"/>
      </linearGradient>
    </defs>
    <path role="img" aria-label="Woman in a sun hat among greenhouse plants" d="M372 82 C 480 70 640 100 700 170 C 735 220 725 330 700 410 C 620 440 500 420 440 380 C 390 340 372 250 372 82 Z" fill="url(#portraitTone)"/>
    <path d="M372 82 C 480 70 640 100 700 170 C 735 220 725 330 700 410" fill="none" stroke="var(--green-dark)" stroke-width="5"/>
    <path d="M700 410 C 620 440 500 420 440 380" fill="none" stroke="var(--green)" stroke-width="4"/>
    <circle role="img" aria-label="Stylist preparing natural ingredients at a table" cx="434" cy="378" r="55" fill="#c9b8a4" stroke="#ffffff" stroke-width="3"/>
    <circle role="img" aria-label="Flat lay of berries and natural treatment products" cx="503" cy="424" r="40" fill="#e3d6d0" stroke="#ffffff" stroke-width="3"/>
    <path d="M0 462 C 130 430 290 440 365 460 C 460 485 600 470 730 448" fill="none" stroke="#d8e43a" stroke-width="5"/>
    <path d="M0 472 C 130 442 290 452 365 470 C 460 495 600 480 730 458 L730 517 L0 517 Z" fill="var(--green)"/>
    <line x1="365" y1="0" x2="365" y2="517" stroke="rgba(0,0,0,.06)" stroke-width="1"/>
  </svg>
  <span class="abs site-url" style="left:22px;top:489px">www.greenhavenstudios.com</span>
  <span class="abs site-url" style="left:551px;top:491px">www.greenhavenstudios.com</span>
</section>

<section class="spread spread--menu">
  <div class="abs menu-bg"></div>
  <div class="abs photo-ingredients" role="img" aria-label="Matcha whisk, bowl and natural powders"></div>
  <div class="abs photo-beach" role="img" aria-label="Woman seen from behind looking out to sea"></div>

  <div class="abs brand" style="left:22px;top:28px"><span class="dot"></span>greenhaven hair studios</div>
  <h1 class="abs menu-title">Our Service Menu</h1>

  <div class="left-col">
    <h2 class="section-head main" style="top:104px">CUT &amp; BLOWDRY</h2>
    <span class="size-head" style="left:185px">S</span><span class="size-head" style="left:218px">M</span><span class="size-head" style="left:253px">L</span><span class="size-head" style="left:285px">XL</span>

    <h3 class="section-head" style="top:134px">LADIES FRINGE</h3>
    <div class="row big" style="top:134px;width:300px"><span class="p s">$77</span><span class="p m">$88</span><span class="p l">$99</span><span class="p xl">$110</span></div>
    <div class="row" style="top:152px">Trim<span class="p s">$25</span></div>
    <div class="row" style="top:163px">Restyle<span class="p s">$35</span></div>

    <h3 class="section-head" style="top:180px">MENS</h3>
    <div class="row" style="top:196px">Single clipper<span class="p s">$28</span></div>
    <div class="row" style="top:207px">Style cut<span class="p s">$42</span></div>

    <h3 class="section-head" style="top:222px">CHILDREN</h3>
    <div class="row" style="top:238px">10 and under<span class="p s">$24</span></div>
    <div class="row" style="top:249px">11-16 Male<span class="p s">$32</span></div>
    <div class="row" style="top:260px">11-16 Female<span class="p s">$48</span></div>
    <div class="row" style="top:271px">add a wash<span class="p s">$5</span></div>

    <h3 class="section-head" style="top:287px">BLOWDRY</h3>
    <div class="row big" style="top:287px"><span class="p s">$47</span><span class="p m">$57</span><span class="p l">$67</span><span class="p xl">$77</span></div>
    <div class="row" style="top:302px">Shampoo &amp; dry off<span class="p s">$25</span></div>

    <h3 class="section-head" style="top:322px">TREATMENTS</h3>
    <div class="row" style="top:337px">Deep treatment<span class="p s" style="top:4px">$35</span></div>
    <div class="row" style="top:348px">Head.Spa ritual<span class="p s" style="top:4px">$65</span></div>

    <h3 class="section-head" style="top:365px">UPSTYLE</h3>
    <div class="row" style="top:378px">45 minutes<span class="p s">$85</span></div>
    <div class="row" style="top:390px">60 minutes<span class="p s">$120</span></div>
  </div>

  <div class="right-col">
    <span class="size-head" style="left:580px">S</span><span class="size-head" style="left:615px">M</span><span class="size-head" style="left:650px">L</span><span class="size-head" style="left:684px">XL</span>

    <h3 class="section-head" style="top:131px">COLOUR</h3>
    <div class="row big" style="top:147px">REGROWTH<span class="p s">$83</span></div>
    <div class="row big" style="top:160px">FULL COLOUR TINT<span class="p s">$125</span><span class="p m">$145</span><span class="p l">$165</span><span class="p xl">$185</span></div>
    <div class="row big" style="top:173px">REGROWTH LIGHTENING*<span class="p s">$165</span><span class="p m">$189</span><span class="p l">$209</span><span class="p xl">$229</span></div>
    <div class="row big" style="top:186px">BALAYAGE/OMBRE*<span class="p m">$275</span><span class="p l">$375</span><span class="p xl">$475</span></div>

    <h3 class="section-head" style="top:207px">BOTANIQ</h3>
    <div class="row big" style="top:227px">REGROWTH<span class="p s">$99</span></div>
    <div class="row big" style="top:238px">FULL COLOUR TINT<span class="p s">$155</span><span class="p m">$175</span><span class="p l">$195</span><span class="p xl">$205</span></div>

    <h3 class="section-head" style="top:255px">FOILS</h3>
    <div class="row big" style="top:270px">SINGLE<span class="p s">$11</span><span class="p m">$13</span><span class="p l">$17</span><span class="p xl">$22</span></div>
    <div class="row big" style="top:281px">1/4 HEAD<span class="p s">$135</span><span class="p m">$155</span><span class="p l">$175</span><span class="p xl">$195</span></div>
    <div class="row big" style="top:292px">1/2 HEAD<span class="p s">$185</span><span class="p m">$205</span><span class="p l">$235</span><span class="p xl">$265</span></div>
    <div class="row big" style="top:303px">FULL HEAD<span class="p s">$235</span><span class="p m">$265</span><span class="p l">$315</span><span class="p xl">$355</span></div>

    <h3 class="section-head" style="top:321px">STRAIGHT</h3>
    <div class="row big" style="top:337px">KERATIN STRAIGHTENING SYSTEM<span class="p s">$335</span><span class="p m">$445</span><span class="p l">$535</span><span class="p xl">$565</span></div>

    <p class="note" style="top:361px">Includes colour match &amp; toner<br>Minimum 6 foils without colour<br>Minimum charge on a Sunday is $40</p>
  </div>

  <svg class="wave" viewBox="0 0 730 517">
    <path d="M0 430 C 200 412 400 418 560 398 C 650 385 705 350 725 322" fill="none" stroke="var(--green-dark)" stroke-width="4"/>
    <path d="M0 440 C 200 424 400 430 560 410 C 650 398 710 365 730 335 L730 517 L0 517 Z" fill="var(--green)"/>
  </svg>
  <p class="abs fine-print">Pricing is indicative of average products used and time taken for each service. You will ALWAYS receive a firm price after your consultation. S to the jaw line I M to the collarbone I L to the bra strap I XL past bra strap</p>
</section>

</body>
</html>
```